A start up special flyer design!

Hi All - Have updated the attachment content - This is the info required for the designs.
I need a catchy flyer to send out to a few areas to advertise the start of my plumbing business!
The flyer will contain an offer for customers, which will need to have some key details on it. See attached. Feel free to fit these criteria into the flyer given your knowledge on design and messaging principles. Key thing to get across to customers is the discount and special offer, and that it is a start up offer.
I have a logo that needs to be on the flyer as well - let me know what format you require and I will send through to you.
The color scheme needs to be blue / grey / black / white.
Let me know if you have any questions.
I

```html
<!DOCTYPE html>
<html lang="en">
<head>
<meta charset="utf-8">
<title>Danny Pipe Plumbing – Start-up Special Flyer</title>
<link href="https://fonts.googleapis.com/css2?family=Jost:wght@500;700&family=Arimo:wght@400;700&family=Questrial&display=swap" rel="stylesheet">
<style>
  :root {
    --blue: #2433a0;
    --blue-light: #3d55c8;
    --blue-dark: #17206b;
    --black: #1d1d1f;
    --grey-light: #f3f3f3;
    --grey-mid: #d6d6d6;
    --white: #ffffff;
    --ink: #111111;
  }
  * { margin: 0; padding: 0; box-sizing: border-box; }
  html, body { width: 1200px; height: 806px; overflow: hidden; background: #e9e9e9; }
  .flyer {
    position: relative; width: 1200px; height: 806px; overflow: hidden;
    background: radial-gradient(ellipse at 70% 35%, var(--grey-light) 0%, #e4e4e4 55%, var(--grey-mid) 100%);
    font-family: "Arimo", Arial, sans-serif;
  }
  .hero-arcs { position: absolute; left: 0; top: 0; width: 1200px; height: 806px; }
  .brand {
    position: absolute; left: 560px; width: 520px; top: 38px; text-align: center;
    font-family: "Jost", sans-serif; font-weight: 700; color: var(--ink);
    font-size: 60px; line-height: 72px; letter-spacing: 1px; text-transform: uppercase;
  }
  .tagline {
    position: absolute; left: 560px; width: 520px; top: 180px; text-align: center;
    font-size: 17px; color: var(--ink);
  }
  .benefits {
    position: absolute; left: 508px; top: 217px; width: 643px; height: 167px;
    background: linear-gradient(90deg, var(--blue-dark) 0%, var(--blue) 45%, var(--blue-light) 100%);
    list-style: none; padding: 22px 0 0 66px;
  }
  .benefits li {
    color: var(--white); font-weight: 700; font-size: 25px; line-height: 48px;
    display: flex; align-items: center; gap: 12px;
  }
  .benefits svg { width: 22px; height: 22px; flex: none; }
  .band-fold { position: absolute; left: 1113px; top: 384px; width: 38px; height: 26px; }
  .offer-box {
    position: absolute; left: 490px; top: 389px; width: 623px; height: 138px;
    background: var(--black); padding: 10px;
  }
  .offer-list {
    list-style: none; border: 1px dashed #cfcfcf; height: 100%;
    padding: 14px 0 0 70px;
  }
  .offer-list li {
    position: relative; color: var(--white); font-size: 17.5px; line-height: 34px;
  }
  .offer-list li::before {
    content: ""; position: absolute; left: -38px; top: 11px;
    width: 12px; height: 12px; border-radius: 50%; background: var(--white);
  }
  .fine-print {
    position: absolute; left: 577px; top: 540px; font-size: 15px; line-height: 26px; color: var(--ink);
  }
  .tools-art {
    position: absolute; left: 395px; top: 562px; width: 180px; height: 140px;
    background: radial-gradient(ellipse at center, #c9c9c9 0%, rgba(200,200,200,0) 70%);
  }
  .booking-strip {
    position: absolute; left: 560px; top: 634px; width: 640px; height: 76px;
    background: var(--white); padding: 10px 0 0 21px;
    font-family: "Questrial", sans-serif; color: var(--blue); font-size: 22px; line-height: 28px;
  }
  .strip-rule { position: absolute; left: 0; width: 1200px; height: 3px; background: var(--blue); }
  .contact-bar {
    position: absolute; left: 0; top: 724px; width: 1200px; height: 82px; background: var(--black);
    display: flex; align-items: center; padding-left: 233px; gap: 36px;
  }
  .contact {
    display: flex; align-items: center; gap: 10px; color: var(--white); font-size: 21px;
  }
  .contact svg { width: 22px; height: 22px; flex: none; }
  .contact.web { margin-left: 18px; }
</style>
</head>
<body>
<main class="flyer">
  <svg class="hero-arcs" viewBox="0 0 1200 806" aria-hidden="false">
    <defs>
      <linearGradient id="photoTone" x1="0" y1="0" x2="1" y2="1">
        <stop offset="0" stop-color="#dfe6f2"/>
        <stop offset="0.35" stop-color="#e7a32c"/>
        <stop offset="0.6" stop-color="#6b8f4a"/>
        <stop offset="1" stop-color="#2a3354"/>
      </linearGradient>
    </defs>
    <ellipse class="arc-blue-outer" cx="130" cy="360" rx="420" ry="520" fill="var(--blue)"/>
    <ellipse class="arc-white" cx="130" cy="360" rx="402" ry="505" fill="var(--white)"/>
    <ellipse class="arc-black" cx="130" cy="360" rx="388" ry="493" fill="var(--black)"/>
    <ellipse class="arc-white-inner" cx="130" cy="360" rx="376" ry="483" fill="var(--white)"/>
    <ellipse class="arc-blue-inner" cx="130" cy="360" rx="366" ry="474" fill="var(--blue)"/>
    <ellipse class="hero-photo" role="img" aria-label="Photo of a plumber holding a yellow hard hat and hammer, wearing a tool belt, in front of a house" cx="130" cy="360" rx="356" ry="465" fill="url(#photoTone)"/>
  </svg>

  <h1 class="brand">Danny Pipe<br>Plumbing</h1>
  <p class="tagline">Delivering Quality Work at a Decent Price</p>

  <ul class="benefits">
    <li><svg viewBox="0 0 24 24"><path d="M2 13l7 7L22 4" fill="none" stroke="#fff" stroke-width="4"/></svg>All plumbing, draining, and gasfitting works</li>
    <li><svg viewBox="0 0 24 24"><path d="M2 13l7 7L22 4" fill="none" stroke="#fff" stroke-width="4"/></svg>“Quality work at a decent price”</li>
    <li><svg viewBox="0 0 24 24"><path d="M2 13l7 7L22 4" fill="none" stroke="#fff" stroke-width="4"/></svg>“Local plumber”</li>
  </ul>
  <svg class="band-fold" viewBox="0 0 38 26" aria-hidden="true"><path d="M0 0H38L0 26Z" fill="var(--blue-dark)"/></svg>

  <section class="offer-box">
    <ul class="offer-list">
      <li>15% off your overall bill*</li>
      <li>No GST payable, saving you additional 10% on your bill^</li>
      <li>Plus, a free hot water health check and replacement quote~</li>
    </ul>
  </section>

  <p class="fine-print">*Offer valid between 15 August 2016 to 15 October 2016<br>^Valid until 30 September 2016.<br>~Quote valid for 12 months from the quote date.</p>

  <div class="tools-art" role="img" aria-label="Illustration of plumbing tools: wrenches, a tap and thread tape"></div>

  <p class="booking-strip">To make an appointment, call or email Danny, or<br>alternatively make&nbsp; a booking directly on the website</p>
  <div class="strip-rule" style="top:710px"></div>
  <div class="strip-rule" style="top:716px;height:2px"></div>

  <footer class="contact-bar">
    <span class="contact phone">
      <svg viewBox="0 0 24 24"><rect width="24" height="24" rx="5" fill="#fff"/><path d="M8 5l2.5 3-1.5 1.8c.9 2 2.3 3.4 4.2 4.3L15 12.6l3 2.4-1.2 3.2C11 18 6 13 5.8 7.1Z" fill="var(--black)"/></svg>
      0400 123 456
    </span>
    <span class="contact email">
      <svg viewBox="0 0 24 24"><rect width="24" height="24" rx="5" fill="#fff"/><rect x="5" y="7" width="14" height="10" fill="none" stroke="var(--black)" stroke-width="1.8"/><path d="M5 7l7 6 7-6" fill="none" stroke="var(--black)" stroke-width="1.8"/></svg>
      danny@dannypipeplumbing.com
    </span>
    <span class="contact web">
      <svg viewBox="0 0 24 24"><rect width="24" height="24" rx="5" fill="#fff"/><circle cx="12" cy="12" r="7" fill="none" stroke="var(--black)" stroke-width="1.6"/><ellipse cx="12" cy="12" rx="3" ry="7" fill="none" stroke="var(--black)" stroke-width="1.4"/><path d="M5 12h14" stroke="var(--black)" stroke-width="1.4"/></svg>
      www.dannypipeplumbing.com
    </span>
  </footer>
</main>
</body>
</html>
```